Looking for a professional, clean and crisp business card

I am in the underground utilities industry and am just looking for a really impressive business card. I would like our card to be white with our symbol crisp and clear with it protruding. I also have a business partner that will require his name and info on the card once the design is set. I would like to have our website info on the card which is;
http://granitetrenchco.example/

Contact Information for Business Card

Website, contact name, number and email

```html
<!DOCTYPE html>
<html lang="en">
<head>
<meta charset="utf-8">
<title>Granite Trench Co — Business Cards</title>
<link href="https://fonts.googleapis.com/css2?family=Play:wght@700&family=Tenor+Sans&family=Mulish:wght@400&display=swap" rel="stylesheet">
<style>
  :root {
    --backdrop: #0a0b0d;
    --card: #ffffff;
    --ink: #111111;
  }
  html, body {
    margin: 0;
    padding: 0;
    width: 848px;
    height: 1200px;
    overflow: hidden;
    background: var(--backdrop);
  }
  .sheet {
    position: relative;
    width: 848px;
    height: 1200px;
  }
  .card {
    position: absolute;
    left: 147px;
    width: 556px;
    height: 343px;
    background: var(--card);
    color: var(--ink);
  }
  .card--first { top: 182px; }
  .card--second { top: 675px; }

  .card__name {
    position: absolute;
    left: 44px;
    top: 28px;
    margin: 0;
    font-family: "Play", sans-serif;
    font-weight: 700;
    font-size: 46px;
    line-height: 50px;
    letter-spacing: 1px;
  }
  .card__rule {
    position: absolute;
    left: 44px;
    top: 131px;
    width: 53px;
    height: 2px;
    background: var(--ink);
  }
  .card__role {
    position: absolute;
    left: 44px;
    top: 138px;
    margin: 0;
    font-family: "Tenor Sans", sans-serif;
    font-size: 18px;
    line-height: 24px;
  }

  .brand {
    position: absolute;
    left: 416px;
    top: 34px;
    width: 118px;
    display: flex;
    flex-direction: column;
    align-items: center;
    gap: 8px;
  }
  .brand__dot {
    width: 54px;
    height: 54px;
    border-radius: 50%;
    background: var(--ink);
  }
  .brand__name {
    font-family: "Play", sans-serif;
    font-weight: 700;
    font-size: 15px;
    line-height: 17px;
    text-align: center;
    color: var(--ink);
  }

  .contact {
    position: absolute;
    left: 318px;
    top: 245px;
    margin: 0;
    padding: 0;
    list-style: none;
    font-family: "Mulish", sans-serif;
    font-size: 12.5px;
  }
  .contact__item {
    display: flex;
    align-items: center;
    height: 23px;
  }
  .contact__icon {
    width: 20px;
    height: 20px;
    margin-right: 8px;
    flex: none;
  }
</style>
</head>
<body>
<main class="sheet">

  <section class="card card--first">
    <h1 class="card__name">Dale<br>Fitzgerald</h1>
    <div class="card__rule"></div>
    <p class="card__role">Granite Trench Co Owner</p>
    <div class="brand">
      <div class="brand__dot"></div>
      <div class="brand__name">Granite Trench Co</div>
    </div>
    <ul class="contact">
      <li class="contact__item">
        <svg class="contact__icon" viewBox="0 0 20 20"><rect x="1" y="4" width="18" height="12" fill="#111"/><polyline points="1.5,4.5 10,11 18.5,4.5" fill="none" stroke="#fff" stroke-width="1.2"/><polyline points="1.5,15.5 7.5,9.5 M12.5,9.5 18.5,15.5" fill="none" stroke="#fff" stroke-width="1"/></svg>
        Dale@granitetrenchco.example
      </li>
      <li class="contact__item">
        <svg class="contact__icon" viewBox="0 0 20 20"><rect x="5" y="1" width="10" height="18" rx="1.5" fill="none" stroke="#111" stroke-width="1.4"/><circle cx="10" cy="16.5" r="0.9" fill="#111"/></svg>
        555-014-2281
      </li>
      <li class="contact__item">
        <svg class="contact__icon" viewBox="0 0 20 20" fill="none" stroke="#111" stroke-width="1.1"><circle cx="10" cy="10" r="8.5"/><ellipse cx="10" cy="10" rx="4" ry="8.5"/><line x1="10" y1="1.5" x2="10" y2="18.5"/><line x1="1.5" y1="10" x2="18.5" y2="10"/><path d="M3 5.5h14M3 14.5h14"/></svg>
        http://granitetrenchco.example
      </li>
    </ul>
  </section>

  <section class="card card--second">
    <h1 class="card__name">Brent<br>Holloway</h1>
    <div class="card__rule"></div>
    <p class="card__role">Granite Trench Co Owner</p>
    <div class="brand">
      <div class="brand__dot"></div>
      <div class="brand__name">Granite Trench Co</div>
    </div>
    <ul class="contact">
      <li class="contact__item">
        <svg class="contact__icon" viewBox="0 0 20 20"><rect x="1" y="4" width="18" height="12" fill="#111"/><polyline points="1.5,4.5 10,11 18.5,4.5" fill="none" stroke="#fff" stroke-width="1.2"/><polyline points="1.5,15.5 7.5,9.5 M12.5,9.5 18.5,15.5" fill="none" stroke="#fff" stroke-width="1"/></svg>
        Brent@granitetrenchco.example
      </li>
      <li class="contact__item">
        <svg class="contact__icon" viewBox="0 0 20 20"><rect x="5" y="1" width="10" height="18" rx="1.5" fill="none" stroke="#111" stroke-width="1.4"/><circle cx="10" cy="16.5" r="0.9" fill="#111"/></svg>
        555-014-2290
      </li>
      <li class="contact__item">
        <svg class="contact__icon" viewBox="0 0 20 20" fill="none" stroke="#111" stroke-width="1.1"><circle cx="10" cy="10" r="8.5"/><ellipse cx="10" cy="10" rx="4" ry="8.5"/><line x1="10" y1="1.5" x2="10" y2="18.5"/><line x1="1.5" y1="10" x2="18.5" y2="10"/><path d="M3 5.5h14M3 14.5h14"/></svg>
        http://granitetrenchco.example
      </li>
    </ul>
  </section>

</main>
</body>
</html>
```